BRAVEN VOLTWORKS SERVICES needs a vibrant design for electrical contracting work.

I require a card design for my own electrical contracting business. I will be doing a lot of domestic and commercial work, including things such as repairs, maintenance, lighting, installations and various others. LED lighting and energy efficiency will be a big part of my business. I wish not to have childish pictures such as light bulbs in the design, but rather a smart and modern looking card which incorporates my logo colours and perhaps the same lighting strike within the faded background of the card.

Target Market(s)

Residential and Commercial property owners.

Industry/Entity Type

Electrical

Contact Information for Business Card

Dario Pesek
EC40362
Phone Number: 0417 538 924
Email: dario@bravenvoltworks.com

Font styles to use
Serif
Sans Serif

Requirements
Must have
• My Logo and associated colours.
Nice to have
• Some form of shapes splitting the card into different colours related to the colours of my logo. Electric Blue, Silver/Grey and White.
Should not have
• Childish pictures and symbols such as light bulbs.

```html
<!DOCTYPE html>
<html lang="en">
<head>
<meta charset="utf-8">
<title>Braven Voltworks Services – Business Card</title>
<link rel="stylesheet" href="https://fonts.googleapis.com/css2?family=Michroma&family=Lato:wght@400;700&display=swap">
<style>
  :root {
    --stage: #161718;
    --card-white: #ffffff;
    --card-shade: #eef0f4;
    --brand-blue: #2f2b8f;
    --brand-violet: #5b57c2;
    --ink: #1e1c6e;
    --rule: #1a1a1a;
    --back-deep: #1b2a7a;
    --back-mid: #2a5fb0;
    --back-light: #4fa3cf;
    --back-text: rgba(210, 225, 245, 0.55);
  }
  * { margin: 0; padding: 0; box-sizing: border-box; }
  html, body { width: 1200px; height: 871px; overflow: hidden; background: var(--stage); }
  .stage { position: relative; width: 1200px; height: 871px; }

  .card {
    position: absolute;
    left: 300px;
    width: 600px;
    height: 343px;
    border-radius: 3px;
    overflow: hidden;
  }
  .card--back { top: 70px; }
  .card--front {
    top: 458px;
    background: linear-gradient(180deg, var(--card-white) 0%, var(--card-white) 60%, var(--card-shade) 100%);
  }

  /* Back */
  .back-art {
    position: absolute; inset: 0;
    background:
      radial-gradient(ellipse at 65% 25%, rgba(120, 200, 230, 0.55), transparent 55%),
      linear-gradient(160deg, var(--back-light) 0%, var(--back-mid) 40%, var(--back-deep) 100%);
  }
  .back-brand {
    position: absolute; left: 60px; top: 120px;
    display: flex; align-items: center; gap: 14px;
    color: var(--back-text);
  }
  .back-brand .mark { flex: none; width: 40px; height: 40px; border-radius: 50%; border: 3px solid var(--back-text); }
  .back-brand .name { font-family: "Michroma", sans-serif; font-size: 22px; line-height: 1.2; letter-spacing: 1px; white-space: nowrap; }
  .back-contact {
    position: absolute; left: 330px; top: 210px;
    font-family: "Lato", sans-serif; font-size: 15px; line-height: 1.5;
    color: var(--back-text);
  }

  /* Front */
  .brand {
    position: absolute; left: 30px; top: 112px;
    width: 270px;
    display: flex; align-items: center; gap: 10px;
    color: var(--brand-blue);
  }
  .brand .mark { flex: none; width: 36px; height: 36px; border-radius: 50%; background: var(--brand-blue); }
  .brand .name {
    font-family: "Michroma", sans-serif;
    font-size: 12.5px; line-height: 1.45; letter-spacing: 0.3px;
    white-space: nowrap;
  }
  .divider {
    position: absolute; left: 322px; top: 70px;
    width: 1.5px; height: 130px; background: var(--rule);
  }
  .contact {
    position: absolute; left: 344px; top: 84px;
    color: var(--ink);
  }
  .contact .person {
    font-family: "Michroma", sans-serif; font-size: 20px; letter-spacing: 2px; line-height: 1.1;
    white-space: nowrap;
  }
  .contact .licence {
    font-family: "Michroma", sans-serif; font-size: 15px; letter-spacing: 3px; margin: 4px 0 10px;
  }
  .contact .line {
    display: flex; align-items: center; gap: 7px;
    font-family: "Lato", sans-serif; font-size: 16px; line-height: 1.45;
    white-space: nowrap;
  }
  .contact svg { flex: none; width: 12px; height: 12px; fill: var(--ink); }
  .band-light {
    position: absolute; left: 0; right: 0; top: 250px; height: 5px;
    background: var(--brand-violet); opacity: 0.75;
  }
  .band-dark {
    position: absolute; left: 0; right: 0; top: 255px; height: 4px;
    background: var(--brand-blue);
  }
</style>
</head>
<body>
<main class="stage">

  <section class="card card--back" aria-label="Business card, back">
    <div class="back-art" role="img" aria-label="Abstract blue light-streak background"></div>
    <div class="back-brand">
      <span class="mark"></span>
      <span class="name">BRAVEN VOLTWORKS<br>SERVICES</span>
    </div>
    <div class="back-contact">
      Dario Pesek<br>EC40362<br>0417 538 924<br>dario@bravenvoltworks.com
    </div>
  </section>

  <section class="card card--front" aria-label="Business card, front">
    <div class="brand">
      <span class="mark"></span>
      <span class="name">BRAVEN VOLTWORKS<br>SERVICES</span>
    </div>
    <div class="divider"></div>
    <div class="contact">
      <p class="person">Dario Pesek</p>
      <p class="licence">EC40362</p>
      <p class="line">
        <svg viewBox="0 0 12 12" aria-hidden="true"><path d="M2.5 0.5h2l1 3-1.4 1a6.5 6.5 0 0 0 3.4 3.4l1-1.4 3 1v2a1 1 0 0 1-1 1A10.5 10.5 0 0 1 1.5 1.5a1 1 0 0 1 1-1z"/></svg>
        0417 538 924
      </p>
      <p class="line">
        <svg viewBox="0 0 12 12" aria-hidden="true"><path d="M0 2h12v8H0z"/><path d="M0.8 2.6 6 6.6l5.2-4" fill="none" stroke="#fff" stroke-width="1"/></svg>
        dario@bravenvoltworks.com
      </p>
    </div>
    <div class="band-light"></div>
    <div class="band-dark"></div>
  </section>

</main>
</body>
</html>
```